Journeys With Marlowe Business Cards

I need a business card design for my upscale Travel Agency.
Attached you can find my logo.
I would like to include the following:
- Name
- Title
- Phone Number
- Email
- Website
- and then something like: Follow us: JourneysWithMarlowe (and then social media icons in color).
The logo should be in the front and then also the back.
I am also attaching a design that I liked (mostly for the layout) but open to any suggestions
Industry/Entity Type
Travel Agent
Contact Information for Business Card
Name: Celine Drummond
Title: Travel Designer / Owner
Phone: 415-296-0487
Email: celine@journeyswithmarlowe.example
Website: www.JourneysWithMarlowe.example
Social Media Handles for FB,IG, Twitter: JourneysWithMarlowe
Font styles to use
Colors
Designer to choose colors to be used in the design.
Look and feel

```html
<!DOCTYPE html>
<html lang="en">
<head>
<meta charset="utf-8">
<title>Journeys With Marlowe – Business Cards</title>
<link rel="stylesheet" href="https://fonts.googleapis.com/css2?family=Poppins:wght@400;500;600&display=swap">
<style>
  :root {
    --backdrop: #ece8e3;
    --card: #ffffff;
    --orange: #f2a65a;
    --orange-deep: #e48d3f;
    --peach: #fbdcbd;
    --peach-light: #fdeedf;
    --ink: #4f4f4f;
    --ink-soft: #5c5c5c;
    --shadow: rgba(60, 40, 20, 0.28);
  }
  * { box-sizing: border-box; margin: 0; padding: 0; }
  html, body { width: 900px; height: 1200px; overflow: hidden; }
  body {
    background: var(--backdrop);
    font-family: "Poppins", sans-serif;
    color: var(--ink);
    position: relative;
  }
  .card {
    position: absolute;
    left: 82px;
    width: 733px;
    height: 429px;
    border-radius: 30px;
    background: var(--card);
    box-shadow: 0 6px 18px var(--shadow);
    overflow: hidden;
  }
  .card--front { top: 138px; }
  .card--back { top: 632px; }

  .brand {
    position: absolute;
    display: flex;
    align-items: center;
    gap: 12px;
    color: var(--orange);
    font-weight: 500;
    white-space: nowrap;
  }
  .brand__square {
    width: 22px;
    height: 22px;
    background: var(--orange);
    flex: none;
  }
  .card--front .brand { left: 44px; top: 196px; font-size: 22px; }

  .divider {
    position: absolute;
    left: 364px;
    top: 124px;
    width: 1px;
    height: 166px;
    background: var(--orange);
  }

  .contact { position: absolute; left: 386px; top: 117px; }
  .contact__name {
    font-size: 20px;
    font-weight: 600;
    color: var(--ink);
    letter-spacing: 0.2px;
    text-transform: uppercase;
    line-height: 1.3;
  }
  .contact__name span { font-weight: 400; }
  .contact__title {
    font-size: 15px;
    font-weight: 500;
    color: var(--orange);
    text-transform: uppercase;
    line-height: 1.4;
    margin-bottom: 17px;
  }
  .contact__list { list-style: none; }
  .contact__item {
    display: flex;
    align-items: center;
    gap: 7px;
    font-size: 15.5px;
    color: var(--ink-soft);
    height: 28.7px;
    white-space: nowrap;
  }
  .contact__icon { width: 17px; height: 17px; flex: none; }
  .contact__dot {
    width: 14px; height: 14px;
    border-radius: 50%;
    background: var(--orange);
    flex: none;
    margin-right: 3px;
  }

  .pattern {
    position: absolute;
    inset: 0;
    background: radial-gradient(ellipse at center, var(--peach-light) 0%, var(--peach) 100%);
  }
  .card--back .brand {
    left: 50%;
    top: 50%;
    transform: translate(-50%, -50%);
    font-size: 30px;
    color: var(--orange-deep);
  }
  .card--back .brand__square { width: 30px; height: 30px; background: var(--orange-deep); }
</style>
</head>
<body>

  <section class="card card--front" aria-label="Business card front">
    <div class="brand">
      <span class="brand__square"></span>
      <span class="brand__name">Journeys With Marlowe</span>
    </div>

    <div class="divider"></div>

    <div class="contact">
      <h1 class="contact__name">Celine <span>Drummond</span></h1>
      <p class="contact__title">Travel Designer / Owner</p>
      <ul class="contact__list">
        <li class="contact__item">
          <svg class="contact__icon" viewBox="0 0 20 20" aria-hidden="true">
            <circle cx="10" cy="10" r="10" fill="var(--orange)"/>
            <path d="M7 5.5c.5-.3 1-.2 1.3.3l.8 1.5c.2.4.1.9-.3 1.2l-.6.4c.5 1.2 1.4 2.1 2.6 2.6l.4-.6c.3-.4.8-.5 1.2-.3l1.5.8c.5.3.6.8.3 1.3-.6 1-1.6 1.5-2.6 1.1C9 12.8 7.2 11 6.2 8.4 5.8 7.3 6.1 6.2 7 5.5z" fill="#fff"/>
          </svg>
          415-296-0487
        </li>
        <li class="contact__item">
          <svg class="contact__icon" viewBox="0 0 20 20" aria-hidden="true">
            <circle cx="10" cy="10" r="10" fill="var(--orange)"/>
            <rect x="5" y="6.5" width="10" height="7" rx="1" fill="#fff"/>
            <path d="M5.3 7l4.7 3.6L14.7 7" fill="none" stroke="var(--orange)" stroke-width="1.1"/>
          </svg>
          celine@journeyswithmarlowe.example
        </li>
        <li class="contact__item">
          <svg class="contact__icon" viewBox="0 0 20 20" aria-hidden="true">
            <circle cx="10" cy="10" r="10" fill="var(--orange)"/>
            <g fill="none" stroke="#fff" stroke-width="1">
              <circle cx="10" cy="10" r="5"/>
              <ellipse cx="10" cy="10" rx="2.2" ry="5"/>
              <path d="M5 10h10M6 7.5h8M6 12.5h8"/>
            </g>
          </svg>
          www.JourneysWithMarlowe.example
        </li>
        <li class="contact__item">
          <span class="contact__dot" aria-hidden="true"></span>
          JourneysWithMarlowe
        </li>
      </ul>
    </div>
  </section>

  <section class="card card--back" aria-label="Business card back">
    <div class="pattern" role="img" aria-label="Peach pattern of small travel icons: landmarks, planes, luggage, palm trees, cameras and maps"></div>
    <div class="brand">
      <span class="brand__square"></span>
      <span class="brand__name">Journeys With Marlowe</span>
    </div>
  </section>

</body>
</html>
```